Vellora - Quality health delivered at your door

Vellora offers home and Community Based Services for adults who wish to continue live independently in their communities. We increase accessibility to health care, reduce health care delivery gap, reduce mortality and morbidity, reduce health while promoting healthy living in the comfort of our patients communities or homes.

We provide on site services and deliver high quality healthcare at your door. Our experienced physicians coordinate care with our certified nurse practitioners and provide chronic care management, physical therapy, rehabilitation and medications management.

Target Market(s)

Older population living in independent living facilities

Industry/Entity Type

Health Care

Contact Information for Business Card

Vellora

Number of Pages Required

4 page

Font styles to use
Sans Serif

Colors

Designer to choose colors to be used in the design.

```html
<!DOCTYPE html>
<html lang="en">
<head>
<meta charset="utf-8">
<title>Vellora - Quality health delivered at your door</title>
<link rel="stylesheet" href="https://fonts.googleapis.com/css2?family=Open+Sans:ital,wght@0,400;0,600;0,700;1,400&family=Raleway:wght@500;600;700&display=swap">
<style>
:root{
  --orange:#f7a11a;
  --green-dark:#1d3a10;
  --green:#4f8a22;
  --green-tile:#1f4a25;
  --ink:#222;
  --body:#666;
  --line:#ddd;
  --white:#fff;
}
*{box-sizing:border-box;margin:0;padding:0}
html,body{width:1200px;height:2651px;overflow:hidden;background:var(--white)}
body{position:relative;font-family:"Open Sans",Arial,sans-serif;color:var(--ink)}
.abs{position:absolute}
h1,h2,h3,h4,.nav a{font-family:"Raleway","Open Sans",sans-serif}

/* header */
.header{left:0;top:0;width:1200px;height:92px;background:var(--white);border-top:4px solid var(--green-dark);z-index:3}
.brand-badge{left:81px;top:-28px;width:208px;height:208px;border-radius:50%;background:var(--white);z-index:4;display:flex;flex-direction:column;align-items:center;justify-content:center;gap:8px;padding-top:30px}
.brand-dot{width:64px;height:64px;border-radius:50%;background:var(--orange)}
.brand-name{font-family:"Raleway",sans-serif;font-weight:600;font-size:30px;color:var(--green-dark)}
.contact-bar{top:14px;right:100px;display:flex;gap:24px;font-size:15px;font-weight:600;z-index:4}
.contact-bar span{display:flex;align-items:center;gap:12px}
.ic-ring{width:32px;height:32px;border-radius:50%;border:1px solid #ccc;display:flex;align-items:center;justify-content:center}
.nav{top:60px;left:0;width:1200px;height:24px;z-index:4;font-size:15px;font-weight:600}
.nav a{color:var(--ink);text-decoration:none;position:absolute;top:0;white-space:nowrap}
.nav a.active{color:var(--orange)}

/* hero */
.hero{left:0;top:92px;width:1200px;height:480px;background:linear-gradient(100deg,#6c8a3a 0%,#9bb46a 35%,#cfd8b0 55%,#7b9a4a 80%,#3f5e22 100%)}
.hero-title{left:100px;top:234px;font-size:50px;font-weight:700;color:var(--white);letter-spacing:1px}
.hero-text{left:100px;top:307px;width:530px;font-size:19px;line-height:30px;font-weight:600;color:var(--white)}
.btn{background:var(--orange);color:var(--white);font-weight:700;border-radius:20px;display:flex;align-items:center;justify-content:center;text-transform:uppercase}
.hero-btn{left:99px;top:428px;width:208px;height:38px;font-size:15px}
.dots{left:566px;top:508px;display:flex;gap:6px}
.dots i{width:14px;height:14px;border-radius:50%;border:2px solid var(--white)}
.dots i.on{background:var(--white)}

/* welcome */
.section-title{width:1200px;left:0;text-align:center;font-size:26px;font-weight:700;text-transform:uppercase;color:var(--ink)}
.welcome-text{left:220px;width:760px;top:712px;text-align:center;font-size:13px;line-height:28px;color:var(--body)}
.feature{width:260px;text-align:center}
.feature svg{display:block;margin:0 auto}
.feature h4{margin-top:30px;font-size:16px;font-weight:700;text-transform:uppercase}
.feature p{margin-top:12px;font-size:12.5px;line-height:23px;color:var(--body)}

/* tiles */
.tile{top:1163px;width:400px;height:349px}
.tile-band{position:absolute;left:0;bottom:0;width:100%;height:91px;display:flex;flex-direction:column;align-items:center;justify-content:center;gap:4px;color:var(--white)}
.tile-band h3{font-size:27px;line-height:32px;font-weight:600;text-transform:uppercase}
.tile-band a{font-size:14px;line-height:18px;font-weight:700;color:var(--white);text-decoration:underline;text-transform:uppercase}

/* blog */
.post-img{width:200px;height:170px;border:1px solid #ccc;padding:4px;background:var(--white)}
.post-img div{width:100%;height:100%}
.post{width:280px}
.post h4{font-size:17px;font-weight:700}
.post .meta{margin-top:12px;font-size:12px;font-style:italic;color:#555;display:flex;gap:8px;align-items:center}
.post p{margin-top:14px;width:252px;font-size:12.5px;line-height:22px;color:var(--body)}
.post .more{display:block;margin-top:14px;font-size:13px;font-weight:700;color:var(--orange);text-transform:uppercase}

/* testimonial */
.testimonial{left:0;top:1942px;width:1200px;height:281px;background:linear-gradient(90deg,#5b4a3e,#a98a72 45%,#8c6e5a 70%,#4a3b31)}
.testimonial::after{content:"";position:absolute;inset:0;background:rgba(40,30,25,.35)}
.avatar{left:111px;top:2014px;width:124px;height:124px;border-radius:50%;border:4px solid var(--white);background:#b8a595;z-index:2}
.quote-rule{left:268px;top:2008px;width:1px;height:138px;background:rgba(255,255,255,.7);z-index:2}
.quote{left:302px;top:2014px;width:790px;font-size:15px;line-height:27px;font-style:italic;color:var(--white);z-index:2}
.quote-name{left:306px;top:2114px;font-family:"Raleway",sans-serif;font-size:19px;font-weight:700;color:var(--white);z-index:2}
.arrow{z-index:2}

/* footer */
.f-brand{left:97px;top:2323px;width:218px;display:flex;flex-direction:column;align-items:center;gap:12px}
.f-brand .brand-dot{width:112px;height:112px;background:var(--orange);border:6px solid var(--green-dark)}
.f-brand .brand-name{font-size:32px}
.f-head{font-family:"Raleway",sans-serif;font-size:19px;font-weight:600;color:var(--ink)}
.f-links{list-style:none;font-size:12.5px;line-height:20.5px;color:#444}
.f-text{font-size:12.5px;line-height:22px;color:#555}
.f-input{left:618px;top:2422px;width:253px;height:32px;border-bottom:1px solid #bbb;font-size:12px;color:#999;padding:8px 12px}
.f-btn{left:617px;top:2469px;width:100px;height:34px;font-size:12px}
.f-contact{left:922px;list-style:none;font-size:12.5px;line-height:20px;color:#444}
.f-contact li{position:absolute;left:0;display:flex;gap:14px;width:260px}
.f-contact svg{flex:none;margin-top:2px}
.f-rule{left:97px;top:2571px;width:1004px;height:1px;background:var(--line)}
.copy{left:97px;top:2601px;font-size:12.5px;color:#555}
.social{top:2595px;left:976px;display:flex;gap:4px}
.social i{width:28px;height:28px;border-radius:50%;border:1px solid #333;display:flex;align-items:center;justify-content:center}
.social i::after{content:"";width:8px;height:8px;border-radius:2px;background:#222}
</style>
</head>
<body>

<header class="abs header"></header>
<div class="abs brand-badge"><span class="brand-dot"></span><span class="brand-name">Vellora</span></div>

<div class="abs contact-bar">
  <span><i class="ic-ring"><svg width="14" height="14" viewBox="0 0 24 24"><path fill="#f7a11a" d="M6.6 10.8a15 15 0 006.6 6.6l2.2-2.2c.3-.3.7-.4 1-.2 1.1.4 2.3.6 3.6.6.6 0 1 .4 1 1V20c0 .6-.4 1-1 1A17 17 0 013 4c0-.6.4-1 1-1h3.5c.6 0 1 .4 1 1 0 1.3.2 2.5.6 3.6.1.3 0 .7-.2 1z"/></svg></i>1 800 555 0142</span>
  <span><i class="ic-ring"><svg width="14" height="14" viewBox="0 0 24 24"><path fill="#f7a11a" d="M2 5h20v14H2zM2 5l10 8 10-8" stroke="#fff" stroke-width="1.5"/></svg></i>info@vellora.com</span>
</div>

<nav class="abs nav">
  <a class="active" style="left:366px">Home</a>
  <a style="left:440px">Assisted Living</a>
  <a style="left:580px">Skilled Nursing</a>
  <a style="left:721px">Independent Living</a>
  <a style="left:894px">Respite Care</a>
  <a style="left:1018px">More</a>
  <svg class="abs" style="left:1086px;top:2px" width="15" height="15" viewBox="0 0 24 24"><circle cx="10" cy="10" r="7" fill="none" stroke="#222" stroke-width="3"/><path d="M15 15l7 7" stroke="#222" stroke-width="3"/></svg>
</nav>

<section class="abs hero" role="img" aria-label="Photo of an elderly man with a walking cane strolling arm in arm with a woman along a leafy park path"></section>
<h1 class="abs hero-title">VELLORA</h1>
<p class="abs hero-text">Vellora offers home and Community Based Services for adults who wish to continue live independently in their communities.</p>
<div class="abs btn hero-btn">Find the right care</div>
<div class="abs dots"><i class="on"></i><i></i><i></i><i></i></div>

<h2 class="abs section-title" style="top:658px">Welcome to Vellora</h2>
<p class="abs welcome-text">We increase accessibility to health care, reduce health care delivery gap, reduce mortality and morbidity, reduce health while promoting healthy living in the comfort of our patients communities or homes.</p>

<div class="abs feature" style="left:77px;top:800px">
  <svg width="166" height="166" viewBox="0 0 166 166"><circle cx="83" cy="83" r="81" fill="none" stroke="#1d3a10" stroke-width="1.5"/><circle cx="83" cy="83" r="73" fill="none" stroke="#1d3a10" stroke-width="5"/>
  <path fill="#f7a11a" d="M60 78h12v32H60zM76 78l12-22c5 0 8 3 7 9l-2 9h16c4 0 6 3 5 7l-5 24c-1 3-3 5-6 5H76z"/></svg>
  <h4>High Quality</h4><p>We increase accessibility to health care, reduce health care delivery gap,</p>
</div>
<div class="abs feature" style="left:338px;top:800px">
  <svg width="166" height="166" viewBox="0 0 166 166"><circle cx="83" cy="83" r="81" fill="none" stroke="#1d3a10" stroke-width="1.5"/><circle cx="83" cy="83" r="73" fill="none" stroke="#1d3a10" stroke-width="5"/>
  <circle cx="83" cy="83" r="26" fill="#f7a11a"/><path d="M71 83l8 8 15-16" fill="none" stroke="#fff" stroke-width="6"/></svg>
  <h4>Reduce Mortality</h4><p>We increase accessibility to health care, reduce health care delivery gap,</p>
</div>
<div class="abs feature" style="left:600px;top:800px">
  <svg width="166" height="166" viewBox="0 0 166 166"><circle cx="83" cy="83" r="81" fill="none" stroke="#1d3a10" stroke-width="1.5"/><circle cx="83" cy="83" r="73" fill="none" stroke="#1d3a10" stroke-width="5"/>
  <g fill="#f7a11a"><circle cx="83" cy="68" r="9"/><circle cx="64" cy="72" r="7"/><circle cx="102" cy="72" r="7"/><path d="M68 102v-14c0-6 5-10 15-10s15 4 15 10v14z"/><path d="M52 100v-10c0-5 4-8 12-8 2 0 4 0 5 1v17zM114 100v-10c0-5-4-8-12-8-2 0-4 0-5 1v17z"/></g></svg>
  <h4>Experienced Physicians</h4><p>We increase accessibility to health care, reduce health care delivery gap,</p>
</div>
<div class="abs feature" style="left:861px;top:800px">
  <svg width="166" height="166" viewBox="0 0 166 166"><circle cx="83" cy="83" r="81" fill="none" stroke="#1d3a10" stroke-width="1.5"/><circle cx="83" cy="83" r="73" fill="none" stroke="#1d3a10" stroke-width="5"/>
  <circle cx="83" cy="83" r="24" fill="none" stroke="#f7a11a" stroke-width="4"/><circle cx="75" cy="77" r="3" fill="#f7a11a"/><circle cx="91" cy="77" r="3" fill="#f7a11a"/><path d="M72 89q11 10 22 0" fill="none" stroke="#f7a11a" stroke-width="4"/></svg>
  <h4>Friendly</h4><p>We increase accessibility to health care, reduce health care delivery gap,</p>
</div>

<div class="abs tile" style="left:0;background:linear-gradient(135deg,#4d6a3a,#b8a48e 55%,#5a7da0)" role="img" aria-label="Photo of a smiling elderly man and a young carer giving thumbs up">
  <div class="tile-band" style="background:var(--green-tile)"><h3>Our Care Services</h3><a>View Services</a></div>
</div>
<div class="abs tile" style="left:400px;background:linear-gradient(135deg,#e8e8e4,#c9b6a6 50%,#6f9ec0)" role="img" aria-label="Photo of a nurse talking with an elderly woman in a wheelchair">
  <div class="tile-band" style="background:var(--orange)"><h3>Find the Right Care</h3><a>Get Started</a></div>
</div>
<div class="abs tile" style="left:800px;background:linear-gradient(135deg,#6f9a4a,#d9c3b0 50%,#3a5f9a)" role="img" aria-label="Photo of a young carer hugging a smiling elderly woman outdoors">
  <div class="tile-band" style="background:var(--green)"><h3>Caring Careers</h3><a>See Jobs Near You</a></div>
</div>

<h2 class="abs section-title" style="top:1604px">Latest Blog</h2>

<div class="abs post-img" style="left:97px;top:1684px"><div style="background:linear-gradient(135deg,#e9e1d8,#c8a894 50%,#5f9fc7)" role="img" aria-label="Photo of a carer helping an elderly woman"></div></div>
<article class="abs post" style="left:323px;top:1680px">
  <h4>Finibus Bonorumet Malorum</h4>
  <div class="meta"><span>▦ 17/07/2017</span><span>|</span><span>● Peter</span></div>
  <p>Nam libero tempore, cum soluta nobis esteli gendi optio cumque nihil impedit quo minus id quod maxime placeat faco.</p>
  <span class="more">Read more &gt;&gt;</span>
</article>
<div class="abs post-img" style="left:626px;top:1684px"><div style="background:linear-gradient(135deg,#6d8e4a,#b59c8c 50%,#c6687a)" role="img" aria-label="Photo of a carer with an elderly man in a wheelchair in a flower garden"></div></div>
<article class="abs post" style="left:852px;top:1680px">
  <h4>Finibus Bonorumet Malorum</h4>
  <div class="meta"><span>▦ 17/07/2017</span><span>|</span><span>● Peter</span></div>
  <p>Nam libero tempore, cum soluta nobis esteli gendi optio cumque nihil impedit quo minus id quod maxime placeat faco.</p>
  <span class="more">Read more &gt;&gt;</span>
</article>

<section class="abs testimonial" role="img" aria-label="Background photo of hands clasped together"></section>
<div class="abs avatar" role="img" aria-label="Portrait photo of the testimonial author"></div>
<div class="abs quote-rule"></div>
<p class="abs quote">Nam libero tempore, cum soluta nobis est eligendi optio cumque nihil impedit quo minus id quod maxime placeat facere possimus, omnis voluptas assumenda est, omnis dolor repellendus. Temporibus autem quibusdam et aut officiis debitis aut rerum necessitatibus saepe eveniet ut et voluptates repudiandae sint et molestiae</p>
<p class="abs quote-name">- Marcel Dufresne</p>
<svg class="abs arrow" style="left:34px;top:2062px" width="20" height="32" viewBox="0 0 20 32"><path d="M16 2L4 16l12 14" fill="none" stroke="rgba(255,255,255,.8)" stroke-width="3"/></svg>
<svg class="abs arrow" style="left:1146px;top:2062px" width="20" height="32" viewBox="0 0 20 32"><path d="M4 2l12 14L4 30" fill="none" stroke="rgba(255,255,255,.8)" stroke-width="3"/></svg>

<footer>
  <div class="abs f-brand"><span class="brand-dot"></span><span class="brand-name">Vellora</span></div>

  <h4 class="abs f-head" style="left:366px;top:2312px">Quick Links</h4>
  <ul class="abs f-links" style="left:366px;top:2354px">
    <li>Home</li><li>Assisted Living</li><li>Skilled Nursing</li><li>Independent Living</li><li>Home &amp; Community Based Services</li><li>Respite Care</li><li>Rehabilitation</li><li>Renova Learning Center</li><li>Renova Learning®</li>
  </ul>

  <h4 class="abs f-head" style="left:618px;top:2312px">Newsletter Subscription</h4>
  <p class="abs f-text" style="left:618px;top:2366px;width:220px">Register your Email Address to get Information about us</p>
  <div class="abs f-input">Email Address</div>
  <div class="abs btn f-btn">Subscribe</div>

  <h4 class="abs f-head" style="left:922px;top:2312px">Contact Us</h4>
  <ul class="abs f-contact" style="top:0">
    <li style="top:2372px"><svg width="12" height="16" viewBox="0 0 12 16"><path d="M6 0a6 6 0 00-6 6c0 4 6 10 6 10s6-6 6-10a6 6 0 00-6-6z" fill="#222"/><circle cx="6" cy="6" r="2" fill="#fff"/></svg><span>Level 14, 220 Harbor Lane<br>Brookfield 4821</span></li>
    <li style="top:2424px"><svg width="14" height="14" viewBox="0 0 24 24"><path fill="#222" d="M6.6 10.8a15 15 0 006.6 6.6l2.2-2.2c.3-.3.7-.4 1-.2 1.1.4 2.3.6 3.6.6.6 0 1 .4 1 1V20c0 .6-.4 1-1 1A17 17 0 013 4c0-.6.4-1 1-1h3.5c.6 0 1 .4 1 1 0 1.3.2 2.5.6 3.6.1.3 0 .7-.2 1z"/></svg><span>1 800 555 0142</span></li>
    <li style="top:2458px"><svg width="14" height="14" viewBox="0 0 14 14"><rect x="0" y="4" width="14" height="10" fill="#222"/><rect x="3" y="0" width="8" height="5" fill="#222"/><rect x="3" y="7" width="8" height="2" fill="#fff"/></svg><span>1 800 555 0199</span></li>
    <li style="top:2492px"><svg width="14" height="12" viewBox="0 0 14 12"><rect width="14" height="12" fill="#222"/><path d="M0 1l7 6 7-6" fill="none" stroke="#fff" stroke-width="1.2"/></svg><span>info@vellora.com</span></li>
  </ul>

  <div class="abs f-rule"></div>
  <p class="abs copy">Copyrights © 2017,&nbsp; Vellora. All rights reserved.</p>
  <div class="abs social"><i></i><i></i><i></i><i></i></div>
</footer>

</body>
</html>
```